KLW Fixings Needs a Packing Design

We need a packing design for products, for example bolts, screws etc.
The accepted design shall be printed in box or cartons made of paper.
We would like to see design that is remarkable and not colourful.
Attached our products photo.

```html
<!DOCTYPE html>
<html lang="en">
<head>
<meta charset="utf-8">
<title>KLW Fixings – Carton Dieline</title>
<link href="https://fonts.googleapis.com/css2?family=Arimo:wght@400;700&family=Roboto+Condensed:wght@700&display=swap" rel="stylesheet">
<style>
  :root {
    --backdrop: #6a7f7e;
    --stock: #ffffff;
    --panel-light: #e4eaea;
    --panel-mid: #b9c6c6;
    --panel-dark: #8fa1a1;
    --ink: #1a1a1a;
    --band-text: #f4f7f7;
  }
  * { margin: 0; padding: 0; box-sizing: border-box; }
  html, body { width: 1200px; height: 1000px; overflow: hidden; background: var(--backdrop); }
  .canvas { position: relative; width: 1200px; height: 1000px; font-family: "Arimo", Arial, sans-serif; }
  .dieline { position: absolute; left: 0; top: 0; }

  .brand-box {
    position: absolute; background: var(--stock);
    display: flex; align-items: center; justify-content: center;
    font-family: "Arimo", Arial, sans-serif; font-weight: 700; color: var(--ink);
    white-space: nowrap;
  }
  .brand-box--large { width: 134px; height: 87px; font-size: 20px; }
  .brand-box--flap { left: 163px; top: 183px; width: 134px; height: 46px; font-size: 15px; flex-direction: column; transform: rotate(180deg); }
  .brand-box--flap .flap-tag { font-size: 9px; margin-top: 2px; }
  .brand-box--band { left: 478px; top: 589px; width: 85px; height: 33px; font-size: 12px; }
  .brand-box--side { left: 1018px; top: 563px; width: 60px; height: 26px; font-size: 10px; justify-content: flex-start; background: transparent; }

  .product-shot {
    position: absolute; width: 236px; height: 118px;
    background: radial-gradient(ellipse at 40% 45%, #a88a55 0%, #9aa3a8 45%, rgba(200,210,210,0) 75%);
  }
  .product-thumb { position: absolute; width: 72px; height: 37px; background: linear-gradient(120deg, #7a6a48, #a89a70 50%, #8f9aa0); }
  .product-thumb--bolt { width: 72px; height: 46px; background: linear-gradient(120deg, #9aa6ad, #c8d0d3 50%, #7f8c93); }

  .band-title {
    position: absolute; font-family: "Roboto Condensed", "Arial Narrow", sans-serif; font-weight: 700;
    font-size: 20px; color: var(--band-text); text-align: center; width: 386px; top: 593px;
  }
  .side-title {
    position: absolute; font-family: "Roboto Condensed", "Arial Narrow", sans-serif; font-weight: 700;
    font-size: 17px; color: var(--ink); top: 375px;
  }
  .company-name { position: absolute; font-size: 12.5px; font-weight: 700; color: var(--ink); }
  .company-details { position: absolute; left: 1021px; top: 614px; font-size: 7px; line-height: 7.6px; color: #333; }
  .flap-line {
    position: absolute; left: 58px; top: 101px; width: 92px; height: 10px;
    font-size: 7px; line-height: 10px; font-weight: 700; color: var(--stock);
    white-space: nowrap; text-align: center;
    transform: rotate(180deg); transform-origin: center center;
  }
  .view-label {
    position: absolute; left: 0; width: 1200px; top: 945px; text-align: center;
    font-size: 40px; font-weight: 700; color: var(--stock);
  }
</style>
</head>
<body>
<div class="canvas">
  <svg class="dieline" width="1200" height="1000" viewBox="0 0 1200 1000" aria-hidden="true">
    <defs>
      <radialGradient id="face" cx="0.45" cy="0.5" r="0.7">
        <stop offset="0" stop-color="#ffffff"/>
        <stop offset="0.55" stop-color="#d3dcdc"/>
        <stop offset="1" stop-color="#aebdbd"/>
      </radialGradient>
      <linearGradient id="band" x1="0" x2="1">
        <stop offset="0" stop-color="#ffffff"/>
        <stop offset="0.25" stop-color="#9dafaf"/>
        <stop offset="0.75" stop-color="#9dafaf"/>
        <stop offset="1" stop-color="#ffffff"/>
      </linearGradient>
      <linearGradient id="flapTone" x1="0" x2="0" y1="0" y2="1">
        <stop offset="0" stop-color="#c9d3d3"/>
        <stop offset="1" stop-color="#b4c2c2"/>
      </linearGradient>
    </defs>

    <polygon points="37,290 5,313 5,650 37,676" fill="var(--stock)"/>

    <path d="M37,86 Q37,64 59,64 L401,64 Q423,64 423,86 L423,870 L310,870 L310,827 L148,827 L148,870 L37,870 Z" fill="var(--stock)"/>
    <rect x="37" y="96" width="386" height="580" fill="url(#flapTone)"/>
    <path d="M37,96 L323,96 Q200,110 37,130 Z" fill="var(--panel-dark)"/>
    <line x1="37" y1="200" x2="423" y2="200" stroke="#ffffff" stroke-width="2"/>
    <rect x="37" y="290" width="386" height="386" fill="url(#face)"/>
    <rect x="37" y="591" width="386" height="29" fill="url(#band)"/>

    <polygon points="430,160 608,160 600,205 617,288 423,288 440,205" fill="var(--stock)"/>
    <rect x="423" y="288" width="194" height="388" fill="var(--stock)"/>
    <polygon points="423,288 617,288 617,300 423,322" fill="var(--panel-dark)"/>
    <rect x="423" y="591" width="194" height="29" fill="url(#band)"/>
    <polygon points="423,676 617,676 598,795 598,870 520,870 520,790 423,676" fill="var(--stock)"/>

    <rect x="617" y="290" width="386" height="386" fill="url(#face)"/>
    <rect x="617" y="591" width="386" height="29" fill="url(#band)"/>
    <polygon points="617,676 1003,676 890,827 890,870 730,870 730,827" fill="var(--stock)"/>

    <polygon points="1010,160 1190,160 1180,205 1200,288 1200,676 1100,795 1100,870 1003,870 1003,288 1020,205" fill="var(--stock)"/>
  </svg>

  <div class="flap-line">KLW Australia PTY LTD</div>
  <div class="brand-box brand-box--flap">KLW Fixings<span class="flap-tag">Bolts, Nuts &amp; Screws</span></div>

  <div class="brand-box brand-box--large" style="left:163px;top:290px;">KLW Fixings</div>
  <div class="product-shot" role="img" aria-label="Photo of flange nuts and hex bolts" style="left:110px;top:440px;"></div>
  <div class="band-title" style="left:37px;">Bolts, Nuts &amp; Screws</div>

  <div class="side-title" style="left:447px;">Bolts, Nuts &amp; Screws</div>
  <div class="product-thumb" role="img" aria-label="Photo of flange nuts" style="left:447px;top:411px;"></div>
  <div class="product-thumb product-thumb--bolt" role="img" aria-label="Photo of hex bolts" style="left:520px;top:449px;"></div>
  <div class="brand-box brand-box--band">KLW Fixings</div>
  <div class="company-name" style="left:454px;top:632px;">KLW Australia PTY LTD</div>

  <div class="brand-box brand-box--large" style="left:743px;top:290px;">KLW Fixings</div>
  <div class="product-shot" role="img" aria-label="Photo of flange nuts and hex bolts" style="left:692px;top:440px;"></div>
  <div class="band-title" style="left:617px;">Bolts, Nuts &amp; Screws</div>

  <div class="side-title" style="left:1028px;">Bolts, Nuts &amp; Screws</div>
  <div class="product-thumb" role="img" aria-label="Photo of flange nuts" style="left:1028px;top:411px;"></div>
  <div class="product-thumb product-thumb--bolt" role="img" aria-label="Photo of hex bolts" style="left:1101px;top:449px;"></div>
  <div class="brand-box brand-box--side">KLW Fixings</div>
  <div class="company-name" style="left:1021px;top:598px;font-size:9.5px;">KLW Australia PTY LTD</div>
  <div class="company-details">[Company Details]<br>Address:<br>Phone:<br>Email:<br>Website:</div>

  <div class="view-label">Full view</div>
</div>
</body>
</html>
```